Schnapsbrennerei sucht neue Etiketten
Zielgruppe
Wir sind eine örtliche Schnapsbrennerei, die inzwischen seit ein paar Jahren einen eigenen Kundenstamm aufgebaut hat. Nun werden wir im nächsten Jahr einen neuen Verkaufsraum bauen. Aus diesem Grund wollen wir unsere Etiketten komplett überarbeiten.
Ein neues Logo habe ich bereits designen lassen. Diese finden Sie unten im Dokumententenupload. Wir legen viel Wert auf eine sehr hohe Qualität, welche sich sowohl in unserem Logo als auch den Etiketten Wiederspiegeln soll.
Unsere Kundschaft ist hauptsächlich Ü35 und legt viel Wert auf hochwertige Produkte.
Aufgabenstellung
Eines direkt vorne weg: Da wir unsere komplette Produktpalette neu gestalten wollen würde ich Sie bitten, der Einfachheit halber zuerst nur ein Schnapsetikett (z.B. Zwetschge oder Willi), ein Likör Etikett und ein Etikett für unseren Whiskey zu erstellen.
Darüber hinaus bitte ich Sie auch ein Design für unseren neuen Gin und einen Aquavit, welcher im Herbst auf den Markt kommen soll zu designen. Im Anschluss daran, werde ich in der Zusammenarbeit mit Ihnen die Etiketten optimieren wollen.
Sobald ein 'Grundetikett' entstanden ist, sollen dann auch die anderen Schnäpse und Liköre in dem gleichen Stil erstellt werden. Explizit möchte ich daraufhin weisen, dass sowohl die Whiskeys als auch der Gin und der Aquavit nicht zwangsläufig das gleiche 'Grundetikett' wie der Schnaps und der Likör haben sollen. Ist bei unseren aktuellen Etiketten auch nicht der Fall. Sehen Sie in den Bildern unten.
Wir verkaufen unseren Schnaps und Likör in 3 unterschieldichen Größen 0,2; 0,5 und 1,0 Liter. Wir verwenden für die 0,2 und 0,5 die Flasche Tessa. Das Etikett der 0,5er Flasche soll in etwa 65x120-130 mm sein. Hier sind wir allerdings variabel.
Dieses entstandene Etikett soll dann auf die anderen Flaschen entsprechend angepasst werden.
Sie finden im Dokumentenupload unsere aktuellen Etiketten und das Logo, welches eingebaut werden soll. Auch ein Etikett von einem örtlichen Weingut, welches mir vom Aufbau und der Unterteilung sehr gut gefällt, werde ich mit anhängen. Allerdings ist dieses Bild sehr unscharf. Wie gesagt es geht hierbei hauptsächlich um die Einteilung mit den oberen und den unteren 'Rahmen'.
Auch unsere Preisliste finden Sie Anhang, wobei diese noch in der Rohform ist und das Obst so nicht verwendet wird, aber hier sind die meisten Produkte drauf.
Das Logo gibt es in verschiedenen Farben. Gerne dürfen Sie für die unterschiedlichen Produkte auch unterschiedliche Farben nutzen.
Was ich mir persönlich g..

```html
<!DOCTYPE html>
<html lang="de">
<head>
<meta charset="utf-8">
<title>Waldhauser's Gin – Etikett</title>
<link href="https://fonts.googleapis.com/css2?family=Bodoni+Moda:wght@500&family=Oswald:wght@400;500&family=Montserrat:wght@500;600&display=swap" rel="stylesheet">
<style>
  :root {
    --backdrop: #d9d9d9;
    --navy: #2b2f3d;
    --navy-deep: #252835;
    --cream: #f6f3ec;
    --gold: #b98a2c;
    --gold-light: #dcb45a;
    --white: #ffffff;
  }
  * { margin: 0; padding: 0; box-sizing: border-box; }
  html, body { width: 1200px; height: 960px; overflow: hidden; background: var(--backdrop); }

  .label {
    position: absolute; left: 220px; top: 40px;
    width: 760px; height: 880px;
    background: var(--cream);
    overflow: hidden;
  }
  .label__main {
    position: absolute; left: 0; top: 0; width: 760px; height: 683px;
    background: linear-gradient(180deg, var(--navy) 0%, var(--navy-deep) 100%);
  }
  .label__frame {
    position: absolute; left: 15px; top: 31px; width: 729px; height: 640px;
    border: 2px solid var(--gold); border-bottom: none;
  }
  .label__tab {
    position: absolute; left: 286px; top: 0; width: 188px; height: 280px;
    background: var(--cream);
  }
  .label__tab-frame {
    position: absolute; left: 20px; top: 31px; width: 148px; height: 226px;
    border: 2px solid var(--gold); border-top: none;
  }
  .brand-mark {
    position: absolute; left: 0; top: 95px; width: 188px;
    display: flex; flex-direction: column; align-items: center; gap: 12px;
  }
  .brand-mark__dot { width: 44px; height: 44px; border-radius: 50%; background: var(--navy); }
  .brand-mark__name {
    font-family: 'Oswald', sans-serif; font-weight: 500; font-size: 22px;
    letter-spacing: 1px; color: var(--navy); text-transform: uppercase;
  }

  .title {
    position: absolute; left: 0; top: 292px; width: 760px; text-align: center;
    font-family: 'Bodoni Moda', serif; font-weight: 500; font-size: 100px; line-height: 1;
    white-space: nowrap;
  }
  .title span {
    display: inline-block; transform: scaleX(0.7);
    background: linear-gradient(180deg, var(--gold-light), var(--gold) 60%, #9a7020);
    -webkit-background-clip: text; background-clip: text; color: transparent;
  }
  .product {
    position: absolute; left: 0; top: 462px; width: 760px; text-align: center;
    font-family: 'Oswald', sans-serif; font-weight: 400; font-size: 84px; line-height: 1;
    color: var(--gold);
  }
  .meta {
    position: absolute; font-family: 'Montserrat', sans-serif; color: var(--white);
  }
  .meta--abv { left: 34px; top: 566px; }
  .meta--abv .meta__value { font-size: 28px; font-weight: 600; letter-spacing: 1px; }
  .meta--abv .meta__note { font-size: 20px; font-weight: 500; margin-top: 4px; }
  .meta--volume { right: 38px; top: 566px; font-size: 28px; font-weight: 600; letter-spacing: 2px; }
  .tagline {
    position: absolute; left: 0; top: 574px; width: 760px; text-align: center;
    font-family: 'Oswald', sans-serif; font-weight: 500; font-size: 30px; line-height: 38px;
    color: var(--white); text-transform: uppercase;
  }

  .label__footer-frame {
    position: absolute; left: 15px; top: 683px; width: 729px; height: 133px;
    border: 2px solid var(--gold); border-top: none;
  }
  .label__rule {
    position: absolute; left: 0; top: 830px; width: 760px; height: 3px; background: var(--gold);
  }
  .producer {
    position: absolute; left: 0; top: 726px; width: 760px; text-align: center;
    font-family: 'Montserrat', sans-serif; font-weight: 500; font-size: 22px; line-height: 32px;
    color: var(--navy); text-transform: uppercase;
  }
</style>
</head>
<body>
  <main class="label">
    <section class="label__main">
      <div class="label__frame"></div>
      <div class="label__tab">
        <div class="label__tab-frame"></div>
        <div class="brand-mark">
          <div class="brand-mark__dot"></div>
          <div class="brand-mark__name">Waldhauser</div>
        </div>
      </div>
      <h1 class="title"><span>WALDHAUSER’S</span></h1>
      <div class="product">GIN</div>
      <div class="meta meta--abv">
        <div class="meta__value">40% vol.</div>
        <div class="meta__note">Spirituose</div>
      </div>
      <p class="tagline">Im Holzfass gereift<br>Special Edition</p>
      <div class="meta meta--volume">0,5 l</div>
    </section>
    <div class="label__footer-frame"></div>
    <p class="producer">Edelbrände &amp; Liköre Konrad Waldhauser<br>Lindenweg 12 - D97412 Haselbach - Telefon 0 94 21 - 3158</p>
    <div class="label__rule"></div>
  </main>
</body>
</html>
```